I need a cover for a brochure made

I need a cover for a brochure. The dimensions are 8.25 wide and 5.25 high... I also need a .25 inch bleed outside of those dimensions.

I need it to look like a vintage photo album cover. In big words, I would like it to say "Family". Above it in smaller words "To our Carrowmere Paddle" ... making it look like the words are gold inlay or something.

I would like it kind of in the style of some of the attached maybe. Just vintage looking.

```html
<!DOCTYPE html>
<html lang="en">
<head>
<meta charset="utf-8">
<title>Family — Brochure Cover</title>
<link href="https://fonts.googleapis.com/css2?family=Pinyon+Script&family=Yellowtail&display=swap" rel="stylesheet">
<style>
  :root {
    --paper: #ffffff;
    --crop: #1a1a1a;
    --leather-light: #b8582c;
    --leather-mid: #8a3d1f;
    --leather-dark: #4a2416;
    --panel-dark: #4e2819;
    --panel-mid: #6b3520;
    --frame-line: #2e150c;
    --frame-highlight: #8a4a2c;
    --gold: #e8b22a;
    --gold-deep: #b07a12;
  }
  html, body {
    margin: 0;
    padding: 0;
    overflow: hidden;
    background: var(--paper);
  }
  .sheet {
    position: relative;
    width: 1200px;
    height: 857px;
    background: var(--paper);
    overflow: hidden;
  }
  .crop-marks {
    position: absolute;
    inset: 0;
  }
  .cover {
    position: absolute;
    left: 100px;
    top: 100px;
    width: 1000px;
    height: 657px;
  }
  .cover-art {
    position: absolute;
    inset: 0;
  }
  .dedication {
    position: absolute;
    left: 0;
    width: 1000px;
    top: 225px;
    text-align: center;
    font-family: "Pinyon Script", cursive;
    font-size: 30px;
    color: var(--gold);
    text-shadow: 0 1px 1px rgba(40, 15, 5, 0.7);
    margin: 0;
  }
  .title {
    position: absolute;
    left: 0;
    width: 1000px;
    top: 268px;
    text-align: center;
    font-family: "Yellowtail", cursive;
    font-size: 118px;
    line-height: 1;
    color: var(--gold);
    text-shadow: 0 2px 0 var(--gold-deep), 0 4px 6px rgba(30, 10, 0, 0.6);
    margin: 0;
    font-weight: 400;
  }
</style>
</head>
<body>
<div class="sheet">
  <svg class="crop-marks" width="1200" height="857" viewBox="0 0 1200 857" aria-hidden="true">
    <g stroke="var(--crop)" stroke-width="1">
      <line x1="133" y1="37" x2="133" y2="72"/>
      <line x1="1065" y1="37" x2="1065" y2="72"/>
      <line x1="133" y1="783" x2="133" y2="819"/>
      <line x1="1065" y1="783" x2="1065" y2="819"/>
      <line x1="37" y1="133" x2="73" y2="133"/>
      <line x1="37" y1="722" x2="73" y2="722"/>
      <line x1="1125" y1="133" x2="1161" y2="133"/>
      <line x1="1125" y1="722" x2="1161" y2="722"/>
    </g>
  </svg>

  <div class="cover">
    <svg class="cover-art" width="1000" height="657" viewBox="0 0 1000 657">
      <defs>
        <radialGradient id="leather" cx="50%" cy="50%" r="70%">
          <stop offset="0%" stop-color="var(--leather-light)"/>
          <stop offset="60%" stop-color="var(--leather-mid)"/>
          <stop offset="100%" stop-color="var(--leather-dark)"/>
        </radialGradient>
        <linearGradient id="panel" x1="0" y1="0" x2="1" y2="1">
          <stop offset="0%" stop-color="var(--panel-mid)"/>
          <stop offset="50%" stop-color="var(--panel-dark)"/>
          <stop offset="100%" stop-color="var(--panel-mid)"/>
        </linearGradient>
        <radialGradient id="cartouche" cx="45%" cy="45%" r="60%">
          <stop offset="0%" stop-color="#c4622e"/>
          <stop offset="70%" stop-color="#9a4520"/>
          <stop offset="100%" stop-color="#6e3018"/>
        </radialGradient>
      </defs>

      <rect class="leather-ground" width="1000" height="657" fill="url(#leather)" role="img" aria-label="Aged cracked leather texture"/>

      <rect class="embossed-panel" x="34" y="35" width="913" height="588" fill="url(#panel)" role="img" aria-label="Embossed scrollwork ornament on dark leather"/>
      <rect x="34" y="35" width="913" height="588" fill="none" stroke="var(--frame-line)" stroke-width="2"/>
      <rect x="42" y="43" width="897" height="572" fill="none" stroke="var(--frame-highlight)" stroke-width="1.5"/>
      <rect x="50" y="51" width="881" height="556" fill="none" stroke="var(--frame-line)" stroke-width="1.5"/>

      <path class="cartouche" d="M170,327 C210,300 240,260 245,220 L245,163 L300,163 C330,163 340,140 360,113 L640,113 C660,140 670,163 700,163 L755,163 L755,220 C760,260 790,300 830,327 C790,354 760,394 755,434 L755,493 L700,493 C670,493 660,516 640,540 L360,540 C340,516 330,493 300,493 L245,493 L245,434 C240,394 210,354 170,327 Z"
            fill="url(#cartouche)" stroke="var(--frame-line)" stroke-width="3"/>
      <path d="M182,327 C220,302 250,262 255,222 L255,173 L302,173 C334,173 346,150 366,123 L634,123 C654,150 666,173 698,173 L745,173 L745,222 C750,262 780,302 818,327 C780,352 750,392 745,432 L745,483 L698,483 C666,483 654,506 634,530 L366,530 C346,506 334,483 302,483 L255,483 L255,432 C250,392 220,352 182,327 Z"
            fill="none" stroke="var(--frame-highlight)" stroke-width="1.5"/>
      <rect x="263" y="163" width="474" height="330" fill="none" stroke="var(--frame-line)" stroke-width="1.5" opacity="0.7"/>
    </svg>

    <p class="dedication">To our Carrowmere Paddle</p>
    <h1 class="title">Family</h1>
  </div>
</div>
</body>
</html>
```